Business card for Tolvery Anesthesia LLC

This is for a business care for Tolvery Anesthesia LLC. Dr. Lisbeth Tolvery, CRNA, DNAP is the sole provider in the LLC. Business address is 4718 N Brackley Street,
Oakhaven, PA 17342
CRNA stands for certified registered nurse anesthetist
"Keeping you safe and comfortable"
I plan to give this business card to the patients that I provide anesthesia to.
Creative design that ties into Anesthesia. Calm soothing colors.

Target Market(s)

Business card for my patients.

Industry/Entity Type

Medicine

Contact Information for Business Card

Creative, professional, eye catching

Logo Text

Tolvery Anesthesia

Font styles to use
Serif
Script

Colors

Designer to choose colors to be used in the design.

Requirements
Must have
• Tolvery Anesthesia
• Dr. Lisbeth Tolvery, CRNA, DNAP
• tolvery.anesthesia@ quillmail.net
Nice to have
• "Keeping you safe and comfortable"
Should not have
• phone number

```html
<!DOCTYPE html>
<html lang="en">
<head>
<meta charset="utf-8">
<title>Tolvery Anesthesia LLC – Business Card</title>
<link rel="stylesheet" href="https://fonts.googleapis.com/css2?family=Montserrat:wght@400;500;600;700&display=swap">
<style>
  :root {
    --backdrop: #d9dcdf;
    --card: #ffffff;
    --brand-blue: #1a78c2;
    --slate: #87888b;
    --slate-line: #8e8f92;
    --slate-light: #c9cacc;
    --orange: #f6941f;
    --orange-deep: #ec6f1f;
    --white: #ffffff;
    --figure-grey: #8a8b8e;
  }
  * { margin: 0; padding: 0; box-sizing: border-box; }
  html, body {
    width: 1200px;
    height: 900px;
    overflow: hidden;
    background: var(--backdrop);
    font-family: "Montserrat", Arial, sans-serif;
  }
  .business-card {
    position: absolute;
    left: 100px;
    top: 160px;
    width: 1000px;
    height: 580px;
    background: var(--card);
    box-shadow: 0 10px 30px rgba(0,0,0,0.18);
    overflow: hidden;
  }
  .card-art { position: absolute; inset: 0; }
  .company-name {
    position: absolute;
    right: 40px;
    top: 128px;
    color: var(--brand-blue);
    font-weight: 600;
    font-size: 32px;
    line-height: 1;
  }
  .provider {
    position: absolute;
    left: 70px;
    top: 318px;
    color: var(--white);
  }
  .provider-name {
    font-weight: 700;
    font-size: 30px;
    line-height: 1.1;
  }
  .provider-credentials {
    font-weight: 400;
    font-size: 18px;
    margin-top: 6px;
    letter-spacing: 0.5px;
  }
  .contact-email {
    position: absolute;
    right: 40px;
    top: 318px;
    color: var(--white);
    font-weight: 400;
    font-size: 21px;
    line-height: 1;
  }
  .tagline {
    position: absolute;
    right: 80px;
    top: 500px;
    color: var(--brand-blue);
    font-weight: 500;
    font-size: 31px;
    line-height: 1;
  }
</style>
</head>
<body>
  <div class="business-card">
    <svg class="card-art" width="1000" height="580" viewBox="0 0 1000 580">
      <line class="top-rule-light" x1="540" y1="182" x2="1000" y2="182" stroke="var(--slate-light)" stroke-width="2"/>
      <line class="top-rule" x1="230" y1="192" x2="1000" y2="192" stroke="var(--slate-line)" stroke-width="4"/>
      <rect class="slate-band" x="495" y="200" width="505" height="160" fill="var(--slate)"/>
      <rect class="band-divider" x="475" y="200" width="20" height="160" fill="var(--orange-deep)"/>
      <rect class="orange-band" x="30" y="270" width="445" height="200" fill="var(--orange)"/>
      <rect class="orange-edge" x="0" y="270" width="30" height="200" fill="var(--orange-deep)"/>
      <rect class="patient-illustration" role="img" aria-label="Illustration of a patient in profile wearing an anesthesia mask"
        x="70" y="130" width="160" height="140" rx="10" fill="var(--figure-grey)"/>
    </svg>

    <div class="company-name">Tolvery Anesthesia LLC</div>
    <div class="contact-email">tolvery.anesthesia@ quillmail.net</div>
    <div class="provider">
      <div class="provider-name">Dr. Lisbeth Tolvery</div>
      <div class="provider-credentials">CRNA, DNAP</div>
    </div>
    <div class="tagline">"Keeping you safe and comfortable"</div>
  </div>
</body>
</html>
```